" A empresa atua em dois segmentos: 1) atendimento psicológico de crianças, adolescentes e adultos e 2) recrutamento, seleçao e treinamento de pessoas. A proposta é trabalhar com o Psicologia e Pessoas em suas diversas dimensoes. "

```html
<!DOCTYPE html>
<html lang="pt-BR">
<head>
<meta charset="UTF-8">
<title>Semear – Papel Timbrado</title>
<link href="https://fonts.googleapis.com/css2?family=Quicksand:wght@500;600&display=swap" rel="stylesheet">
<style>
  :root {
    --backdrop: #e4e1dc;
    --paper: #ffffff;
    --teal: #17a89e;
    --teal-dark: #12968d;
    --mark-grey: #ebebec;
  }
  html, body {
    margin: 0;
    padding: 0;
    width: 1200px;
    height: 1200px;
    overflow: hidden;
    background: var(--backdrop);
    font-family: "Quicksand", sans-serif;
  }
  .letterhead {
    position: absolute;
    left: 232px;
    top: 80px;
    width: 735px;
    height: 1040px;
    background: var(--paper);
    box-shadow: 0 6px 22px rgba(0, 0, 0, 0.25);
    overflow: hidden;
  }
  .brand {
    position: absolute;
    top: 46px;
    left: 0;
    width: 100%;
    display: flex;
    flex-direction: column;
    align-items: center;
  }
  .brand-dot {
    width: 70px;
    height: 70px;
    border-radius: 50%;
    background: var(--teal-dark);
  }
  .brand-name {
    margin-top: 6px;
    font-size: 27px;
    font-weight: 600;
    color: var(--teal);
    line-height: 1;
    letter-spacing: 0.5px;
  }
  .brand-tagline {
    margin-top: 3px;
    font-size: 10px;
    font-weight: 500;
    color: var(--teal);
    letter-spacing: 0.6px;
  }
  .corner-mark {
    position: absolute;
    left: 420px;
    top: 700px;
    width: 300px;
    height: 300px;
    border-radius: 50%;
    background: var(--mark-grey);
  }
  .footer-band {
    position: absolute;
    left: 0;
    top: 965px;
    width: 100%;
    height: 43px;
    background: var(--teal);
  }
  .contact {
    position: absolute;
    left: 19px;
    top: 874px;
    margin: 0;
    font-style: normal;
    font-size: 11.5px;
    font-weight: 500;
    line-height: 16px;
    color: var(--teal);
  }
</style>
</head>
<body>
  <main class="letterhead">
    <header class="brand">
      <div class="brand-dot"></div>
      <div class="brand-name">Semear</div>
      <div class="brand-tagline">Psicologia e Pessoas</div>
    </header>

    <div class="corner-mark"></div>
    <div class="footer-band"></div>

    <address class="contact">
      Rua das Acácias nº 210<br>
      São Paulo &nbsp;SP<br>
      11 4032-7781<br>
      11 4032-7790<br>
      www.semearpsi.com.br
    </address>
  </main>
</body>
</html>
```